Analytics/BI tech start-up seeks sharp, creative, simple, secret agent type logo & theme

"Quarry 7 Technologies" seeks a logo design/color scheme template for NYC based tech start-up of software engineers, solutions architects, and data/BI analysts. We develop reporting solutions and analytics platforms for small-medium sized businesses. We code for database, cloud, and web/mobile apps.<br/><br/>Some *very basic, limited* sketches are attached to show ideas we've had. We need a logo and color scheme that may be used for business cards, paper letterhead and envelopes, and web pages to be published at "www.quarry7.dev".<br/><br/>We like the black/red, red/white, blue/black, white/black contrasts as a stating point, and prefer black background business cards, but open to anything if it feels like a good match. We are relying on the projects submitted here to take care of the creativity part of our image, which we work on logistics to launching our start-up. Something that could also be easily translated into black/white, grayscale would be appreciated as well. while log is important, we also need an icon that may be used as an app thumbnail. For font, we prefer all caps.<br/><br/>Business: Quarry 7 Technologies<br/>Slogan: If. Else. Us. / If -> Else -> Us / If - Else - Us / etc.<br/>Website: www.quarry.dev<br/>Icon: [Q7] , only as a starting point<br/>Theme Ideas: Sleek, futuristic, secret agent-like tech, simple, bold color contrasts, software code related<br/><br/>Feel free to reach out to jvorenko@mailbarn.example as a contact for any questions or follow up. We look forward to seeing amazing ideas!
Updates

We would like to provide the opportunity for as many different submissions as possible.

Target Market(s)

Small business owners, entrepreneurs, financial/tech companies, freelance engineers, people in need of IT assistance to elevate business

Industry/Entity Type

It Company

Contact Information for Business Card

Individual Info: Name, Position, Phone Number 1, Phone Number 2 (optional), Fax Number, email Address.
Company Info: Name, logo, icon (optional), web site, slogan

Font styles to use
Sans Serif
Other font styles liked:
• Similar to Biome Light All Caps, Hollow Meridian type style

Requirements
Must have
• Pronounced 1 in the logo, either in the word Section or not. Bold color contrast, one side with only logo or icon, possible web address too. Other side with all individual info plus logo, and/or icon and web address. If using uploaded files as a base, center the C more between the E and T, it is too closer to the T as is.
Nice to have
• Bolder font possibly, more square edged at ends of letters but still with minor curved corners. Icon suggested as a starting point is “[Q7]” and instead of a slogan, use "Data - Cloud - Web - Software" and the dividers don't necessary have to be hyphens.
Should not have
• Open to all creative ideas, try anything. Please come up with different logos than are in the attached files, they are meant as a starting point.

```html
<!DOCTYPE html>
<html lang="en">
<head>
<meta charset="utf-8">
<title>Quarry 7 Technologies – Business Card</title>
<link rel="stylesheet" href="https://fonts.googleapis.com/css2?family=Open+Sans:wght@400;700&family=Roboto:wght@400&display=swap">
<style>
  :root {
    --backdrop: #d8d3cd;
    --navy-deep: #0b2350;
    --navy: #12337a;
    --blue-bright: #2a63c9;
    --frost: #dcd9d5;
    --frost-light: #ebe9e6;
    --ink-light: #dfe4ee;
    --ink-soft: #c9d3e6;
    --brand-navy: #132f6b;
  }
  * { box-sizing: border-box; margin: 0; padding: 0; }
  html, body { width: 1200px; height: 969px; overflow: hidden; }
  body { background: var(--backdrop); position: relative; }

  .card {
    position: absolute; left: 155px; top: 222px;
    width: 918px; height: 524px;
    background: var(--navy-deep);
    box-shadow: 0 10px 30px rgba(0,0,0,.18);
    overflow: hidden;
  }
  .card__info-side {
    position: absolute; left: 0; top: 0; width: 475px; height: 100%;
    background: radial-gradient(ellipse 70% 80% at 55% 35%, var(--blue-bright), var(--navy) 60%, var(--navy-deep) 100%);
  }
  .card__shade {
    position: absolute; left: 420px; top: 0; width: 60px; height: 100%;
    background: linear-gradient(90deg, transparent, var(--navy-deep));
  }
  .card__frame { position: absolute; left: 473px; top: 0; }

  .holder { position: absolute; left: 52px; color: var(--ink-light); }
  .holder__name {
    top: 66px; font: 700 29px/1 "Open Sans", sans-serif; letter-spacing: .5px;
  }
  .holder__title {
    top: 104px; font: 400 20px/1 "Open Sans", sans-serif; color: var(--ink-soft);
  }
  .address { top: 240px; font: 400 22px/31px "Roboto", sans-serif; }
  .contacts { top: 325px; list-style: none; font: 400 22px/30.5px "Roboto", sans-serif; }
  .contacts li { display: flex; align-items: center; }
  .contacts svg { width: 20px; height: 20px; margin-right: 15px; fill: var(--ink-light); }

  .brand-name {
    position: absolute; left: 479px; top: 248px; width: 424px;
    text-align: center; color: var(--brand-navy);
    font: 700 25px/1 "Open Sans", sans-serif; letter-spacing: 1px;
  }
</style>
</head>
<body>
  <div class="card">
    <div class="card__info-side"></div>
    <div class="card__shade"></div>
    <svg class="card__frame" width="445" height="524" viewBox="0 0 445 524" aria-hidden="true">
      <defs>
        <radialGradient id="frostGlow" cx="0.55" cy="0.3" r="0.6">
          <stop offset="0" stop-color="var(--frost-light)"/>
          <stop offset="1" stop-color="var(--frost)" stop-opacity="0"/>
        </radialGradient>
      </defs>
      <rect x="0" y="0" width="445" height="524" fill="var(--navy-deep)"/>
      <rect x="6" y="16" width="424" height="492" fill="var(--frost)"/>
      <rect x="94" y="0" width="241" height="524" fill="var(--frost)"/>
      <rect x="6" y="16" width="424" height="492" fill="url(#frostGlow)"/>
    </svg>

    <div class="holder holder__name">DANIEL ARCHER</div>
    <div class="holder holder__title">President</div>

    <div class="holder address">4120 Alder Court<br>Anchorage, Alaska 99501</div>

    <ul class="holder contacts">
      <li><svg viewBox="0 0 20 20"><path d="M4 2l3 0 2 4-2 2c1 2 3 4 5 5l2-2 4 2v3c0 1-1 2-2 2C9 18 2 11 2 4c0-1 1-2 2-2z"/></svg>555-201-0148</li>
      <li><svg viewBox="0 0 20 20"><path d="M6 1h8a1 1 0 011 1v16a1 1 0 01-1 1H6a1 1 0 01-1-1V2a1 1 0 011-1zm1 2v12h6V3z"/></svg>555-201-0172</li>
      <li><svg viewBox="0 0 20 20"><path d="M5 2h10v5H5zM2 8h16v7h-3v3H5v-3H2zm5 5v3h6v-3z"/></svg>555-201-0190</li>
      <li><svg viewBox="0 0 20 20"><path d="M2 5h16v10H2zm1 1l7 5 7-5z" fill-rule="evenodd"/></svg>info@quarry7tech.example</li>
      <li><svg viewBox="0 0 20 20"><path d="M10 1a9 9 0 100 18 9 9 0 000-18zm-1 2c-2 2-3 4-2 6l3 1 1 3-2 2 1 2a7 7 0 01-7-7c0-3 2-6 6-7zm3 0a7 7 0 015 10l-2-2 1-3-3-2z"/></svg>quarry7tech.example</li>
    </ul>

    <div class="brand-name">QUARRY 7 TECHNOLOGIES</div>
  </div>
</body>
</html>
```